Health care equipment supplier needs a new website design

Our old website is tired but visiting it will give you a wealth of information about our products and services.

The why of my business:
Simply, I wanted to take the CRAP out of CPAP
Being told I needed to spend well over $2,000 for treatment was bullshit. The available options were limited, and all too expensive.
I wanted to know more, but was told very little.
I needed help, but didn't know who to trust.
I felt there must be a better way - but there wasn't.

We help thousands of people each year get a great night's sleep. Our customers wake up every morning feeling refreshed and energised, ready to take on the world.

The what of our business; Based on experience, we have a proven system for product selection and customer care that makes sleep apnea healthcare much more affordable.

Eventually, our new website will feature a combination of platforms such as wordpress (for us to easy edit sections) and an e-commerce cart like Magento to process online shop orders.

The brief
-----------
Provide a modern, home page design that considers the following requirements;

Emotional landing page that explains the 'why' of our business and builds trust.

Colours: Ideally Blue, grey, white being the colours of our logo

High contrast, large size font to cater for our more elderly demographic.
Search bar (at top of page)
The why of our business (text and video introduction)
Tops Sellers
Premium Range
Testimonials
Stay up to date - join our mailing list and receive $50 discount
Contact phone and email address clearly visible

Menu options
* About Us
* Contact Us
* Franchise
* New Arrivals
* Finance
* SHOP

The Home Page design theme will need to be adapted over the following pages in the future;
2. About Us
3. News Header (index of news article)
4. News Detail (show news article clicked from 3 above)
5. Shop Home Page
6. Shop Catalog Page - BOXES
7. Shop Catalog Page - LINES
8. Shop Product Page
9. Shopping Cart Page
10. Checkout Page
11. Customer Profile Page (self service account management)
12. FAQ Page

Target Market(s)

Age: 35~75
70% male

Industry/Entity Type

Health Care

Number of Pages Required

1 page

Font styles to use
Sans Serif

Requirements
Must have
• Emotional landing page that explains the 'why' of our business and builds trust.
• High contrast, large size font to cater for our more elderly demographic.
• Search bar (at top of page)
• The why of our business (text and video introduction)
• Tops Sellers
• Premium Range
• Testimonials
• Stay up to date - join our mailing list and receive $50 discount
• Contact phone and email address clearly visible
• Main Menu items\Menu options
• * About Us
• * Contact Us
• * Franchise
• * New Arrivals
• * Finance
• * SHOP
Nice to have
• Ideally Blue, grey, white being the colours of our logo
Should not have
• small font
• hard to read font
• Black backgound

```html
<!DOCTYPE html>
<html lang="en">
<head>
<meta charset="utf-8">
<title>RestWell Supply — Health Care Equipment</title>
<link href="https://fonts.googleapis.com/css2?family=Open+Sans:wght@400;600;700;800&display=swap" rel="stylesheet">
<style>
:root{
  --blue:#2c4a9a;
  --blue-dark:#223b80;
  --cyan:#1e9bd7;
  --nav:#4a4a4a;
  --nav-active:#2c4a9a;
  --grey-bg:#f1f1f1;
  --grey-line:#dddddd;
  --text:#333333;
  --muted:#777777;
  --red:#d9302c;
  --white:#ffffff;
}
*{box-sizing:border-box;margin:0;padding:0}
html,body{width:1200px;height:2824px;overflow:hidden}
body{font-family:"Open Sans",Arial,sans-serif;color:var(--text);background:var(--white)}
.wrap{width:1200px;position:relative}
a{color:inherit;text-decoration:none}

/* header */
.site-header{height:140px;display:flex;align-items:center;padding:0 132px;justify-content:space-between}
.brand{display:flex;align-items:center;gap:12px;font-weight:800;font-size:30px;color:var(--blue)}
.brand-mark{width:40px;height:40px;background:var(--blue)}
.search{display:flex;height:44px;border:2px solid var(--blue)}
.search select,.search input{border:0;font:14px "Open Sans",sans-serif;color:var(--muted);padding:0 12px;background:#fff}
.search select{width:90px;border-right:1px solid var(--grey-line)}
.search input{width:240px}
.search button{border:0;background:var(--blue);color:#fff;font:700 13px "Open Sans",sans-serif;padding:0 18px;text-transform:uppercase}
.contact{font-size:14px;font-weight:600;color:var(--text);display:flex;flex-direction:column;gap:6px}
.contact span{display:flex;align-items:center;gap:8px}

/* nav */
.main-nav{height:48px;background:var(--nav);display:flex;padding:0 132px}
.main-nav a{color:#fff;font-size:15px;font-weight:600;padding:0 28px;line-height:48px}
.main-nav a.active{background:var(--nav-active)}

/* hero */
.hero{height:520px;position:relative;background:linear-gradient(90deg,#e8eaec 0%,#f4f5f6 55%,#e9ecef 100%);overflow:hidden}
.hero-photo{position:absolute;left:0;top:0;width:720px;height:520px;background:linear-gradient(120deg,#c9b9a8 0%,#e2cfc0 40%,#d7d9de 100%)}
.hero-copy{position:absolute;left:760px;top:90px;width:400px;text-align:right}
.hero-copy h1{font-size:54px;font-weight:700;line-height:1.1;color:var(--cyan)}
.hero-copy h1 span{display:block;color:var(--text)}
.hero-copy p{margin-top:12px;font-size:17px;color:var(--muted)}
.hero-product{position:absolute;left:780px;top:290px;width:330px;height:200px;background:linear-gradient(160deg,#3a3d42,#15171a);border-radius:26px}
.dots{position:absolute;right:142px;top:262px;display:flex;gap:8px}
.dots i{width:10px;height:10px;border-radius:50%;background:#bbb}
.dots i:first-child{background:var(--blue)}

/* why */
.why{height:492px;background:var(--grey-bg);padding-top:64px}
.section-title{text-align:center;font-size:36px;font-weight:700;color:var(--text)}
.why-body{display:flex;gap:56px;padding:0 132px;margin-top:46px}
.video{width:476px;height:292px;background:linear-gradient(160deg,#2a2c30,#0e0f11);position:relative}
.video-bar{position:absolute;left:0;right:0;bottom:0;height:28px;background:#111;display:flex;align-items:center;gap:10px;padding:0 10px;color:#ccc;font-size:11px}
.video-bar .track{flex:1;height:4px;background:#555}
.why-text{flex:1}
.why-text ul{list-style:none}
.why-text li{display:flex;gap:10px;font-size:15px;line-height:1.45;margin-bottom:8px}
.why-text li svg{flex:none;margin-top:4px}
.why-text p{font-size:15px;line-height:1.5;margin-top:10px}
.btn{display:inline-block;background:var(--blue);color:#fff;font-weight:700;font-size:15px;padding:12px 26px;margin-top:18px}

/* top sellers */
.sellers{height:560px;padding-top:80px;position:relative}
.section-sub{text-align:center;font-size:15px;color:var(--muted);width:760px;margin:14px auto 0;line-height:1.5}
.cards{display:flex;gap:20px;padding:0 132px;margin-top:40px}
.card{width:221px;border:1px solid var(--grey-line);padding:14px;text-align:center;height:328px;position:relative}
.save{position:absolute;right:14px;top:10px;font-size:12px;font-weight:700;color:var(--red)}
.card-img{height:130px;margin:22px 0 14px;background:linear-gradient(160deg,#e3e6ea,#b9bec6)}
.card h3{font-size:15px;font-weight:600;line-height:1.35;height:42px}
.price{margin-top:10px;font-size:18px;font-weight:700;color:var(--red)}
.price s{color:var(--muted);font-weight:400;font-size:14px;margin-right:8px}
.btn-sm{display:inline-block;background:var(--blue);color:#fff;font-size:13px;font-weight:700;padding:9px 20px;margin-top:12px}
.arrow{position:absolute;top:376px;width:34px;height:34px;border-radius:50%;background:#ddd;display:flex;align-items:center;justify-content:center}
.arrow.left{left:86px}.arrow.right{right:86px}

/* premium */
.premium{height:432px;position:relative;background:linear-gradient(90deg,#f5f5f5 0%,#eeeff1 60%,#e4e7ec 100%);overflow:hidden}
.premium-photo{position:absolute;right:0;top:0;width:560px;height:432px;background:linear-gradient(90deg,rgba(238,239,241,1),rgba(214,206,200,.7));}
.premium-product{position:absolute;left:132px;top:70px;width:430px;height:260px;background:linear-gradient(160deg,#3b3e44,#121315);border-radius:30px}
.premium-copy{position:absolute;left:600px;top:70px;width:468px}
.premium-copy h2{font-size:34px;font-weight:700}
.premium-copy .amount{font-size:30px;font-weight:700;color:var(--red);margin-top:6px}
.premium-copy .amount small{font-size:15px;color:var(--muted);font-weight:600}
.premium-copy p{font-size:14px;line-height:1.55;color:#555;margin-top:14px}

/* testimonials */
.testimonials{height:308px;background:var(--blue);color:#fff;padding-top:40px}
.testimonials .section-title{color:#fff}
.quotes{display:flex;padding:0 132px;margin-top:34px;gap:0}
.quote{flex:1;padding:0 40px;font-size:14px;line-height:1.55}
.quote + .quote{border-left:1px solid rgba(255,255,255,.35)}
.author{display:flex;align-items:center;gap:16px;margin-top:18px}
.avatar{width:56px;height:56px;border-radius:50%;background:linear-gradient(160deg,#d6dbe6,#8e9ab8);border:3px solid #fff}
.author b{display:block;font-size:14px}
.stars{display:flex;gap:3px;margin-top:4px}

/* newsletter */
.newsletter{height:180px;display:flex;align-items:center;justify-content:space-between;padding:0 132px;border-bottom:1px solid var(--grey-line)}
.newsletter h2{font-size:34px;font-weight:700}
.newsletter p{font-size:20px;margin-top:4px}
.newsletter p b{color:var(--red)}
.subscribe{display:flex;height:48px}
.subscribe input{width:260px;border:1px solid #ccc;padding:0 14px;font:14px "Open Sans",sans-serif}
.subscribe button{border:0;background:var(--red);color:#fff;font:700 15px "Open Sans",sans-serif;padding:0 24px}

/* footer */
.site-footer{height:144px;display:flex;align-items:center;padding:0 132px;gap:40px}
.footer-links{flex:1;font-size:13px;color:var(--muted);line-height:1.8}
.follow{display:flex;align-items:center;gap:8px;font-size:13px;color:var(--muted)}
.follow i{width:26px;height:26px;border-radius:50%;background:var(--blue)}
.follow i:nth-child(3){background:var(--cyan)}
.follow i:nth-child(4){background:var(--red)}
.follow i:nth-child(5){background:#e07b28}
</style>
</head>
<body>
<div class="wrap">

<header class="site-header">
  <a class="brand" href="#"><span class="brand-mark"></span>RestWell Supply</a>
  <form class="search">
    <select><option>All</option></select>
    <input type="text" value="Search products...">
    <button type="button">Search</button>
  </form>
  <div class="contact">
    <span><svg width="14" height="14" viewBox="0 0 24 24"><path fill="#2c4a9a" d="M6.6 10.8a15 15 0 0 0 6.6 6.6l2.2-2.2c.3-.3.7-.4 1-.2 1.1.4 2.3.6 3.6.6.6 0 1 .4 1 1V20c0 .6-.4 1-1 1A17 17 0 0 1 3 4c0-.6.4-1 1-1h3.5c.6 0 1 .4 1 1 0 1.3.2 2.5.6 3.6.1.3 0 .7-.2 1z"/></svg>1800 555 0142</span>
    <span><svg width="14" height="14" viewBox="0 0 24 24"><path fill="#2c4a9a" d="M2 5h20v14H2zm2 2v.5l8 5 8-5V7z"/></svg>hello@restwellsupply.example</span>
  </div>
</header>

<nav class="main-nav">
  <a class="active" href="#">Home</a>
  <a href="#">About Us</a>
  <a href="#">Contact Us</a>
  <a href="#">Franchise</a>
  <a href="#">New Arrivals</a>
  <a href="#">Finance</a>
  <a href="#">SHOP</a>
</nav>

<section class="hero">
  <div class="hero-photo" role="img" aria-label="Smiling senior couple resting cheek to cheek"></div>
  <div class="hero-copy">
    <h1>Health Care <span>Equipment</span></h1>
    <p>Restful sleep therapy, supplied with care and honest prices.</p>
  </div>
  <div class="dots"><i></i><i></i><i></i><i></i></div>
  <div class="hero-product" role="img" aria-label="Sleep therapy machine with humidifier"></div>
</section>

<section class="why">
  <h2 class="section-title">Why of Our Business</h2>
  <div class="why-body">
    <div class="video" role="img" aria-label="Introduction video showing a sleep therapy machine">
      <div class="video-bar">
        <svg width="12" height="12" viewBox="0 0 12 12"><path fill="#ccc" d="M2 1l9 5-9 5z"/></svg>
        <span>0:00 / 2:40</span><span class="track"></span>
        <svg width="12" height="12" viewBox="0 0 12 12"><rect x="1" y="1" width="10" height="10" fill="none" stroke="#ccc"/></svg>
      </div>
    </div>
    <div class="why-text">
      <ul>
        <li><svg width="14" height="14" viewBox="0 0 14 14"><path d="M2 7l3 3 7-7" fill="none" stroke="#2c4a9a" stroke-width="2"/></svg>Simply, I wanted to take the crap out of CPAP.</li>
        <li><svg width="14" height="14" viewBox="0 0 14 14"><path d="M2 7l3 3 7-7" fill="none" stroke="#2c4a9a" stroke-width="2"/></svg>Being told I needed to spend well over $2,000 for treatment was wrong. The options were limited.</li>
        <li><svg width="14" height="14" viewBox="0 0 14 14"><path d="M2 7l3 3 7-7" fill="none" stroke="#2c4a9a" stroke-width="2"/></svg>All too expensive for most people.</li>
        <li><svg width="14" height="14" viewBox="0 0 14 14"><path d="M2 7l3 3 7-7" fill="none" stroke="#2c4a9a" stroke-width="2"/></svg>I wanted to know more, but was told very little.</li>
        <li><svg width="14" height="14" viewBox="0 0 14 14"><path d="M2 7l3 3 7-7" fill="none" stroke="#2c4a9a" stroke-width="2"/></svg>I needed help, but didn't know who to trust.</li>
        <li><svg width="14" height="14" viewBox="0 0 14 14"><path d="M2 7l3 3 7-7" fill="none" stroke="#2c4a9a" stroke-width="2"/></svg>I felt there must be a better way, but there wasn't.</li>
      </ul>
      <p>We help thousands of people each year get a great night's sleep, with a proven system that makes care affordable.</p>
      <a class="btn" href="#">View More Information</a>
    </div>
  </div>
</section>

<section class="sellers">
  <h2 class="section-title">Tops Sellers</h2>
  <p class="section-sub">Our most trusted sleep therapy products, chosen by customers who wake up refreshed and ready for the day, at prices that make sense.</p>
  <span class="arrow left"><svg width="12" height="12" viewBox="0 0 12 12"><path d="M8 1L3 6l5 5" fill="none" stroke="#666" stroke-width="2"/></svg></span>
  <span class="arrow right"><svg width="12" height="12" viewBox="0 0 12 12"><path d="M4 1l5 5-5 5" fill="none" stroke="#666" stroke-width="2"/></svg></span>
  <div class="cards">
    <article class="card"><span class="save">Save 27% off</span><div class="card-img" role="img" aria-label="Travel machine starter kit"></div><h3>Nightline II Machine Starter Kit</h3><div class="price"><s>$940.00</s>$690.00</div><a class="btn-sm" href="#">Add to Cart</a></article>
    <article class="card"><span class="save">Save 27% off</span><div class="card-img" role="img" aria-label="Machine with humidifier and mask"></div><h3>Harbor Auto Machine with Humidifier</h3><div class="price"><s>$940.00</s>$690.00</div><a class="btn-sm" href="#">Add to Cart</a></article>
    <article class="card"><span class="save">Save 27% off</span><div class="card-img" role="img" aria-label="Coiled air tubing"></div><h3>Nightline II Machine Starter Kit</h3><div class="price"><s>$940.00</s>$690.00</div><a class="btn-sm" href="#">Add to Cart</a></article>
    <article class="card"><span class="save">Save 27% off</span><div class="card-img" role="img" aria-label="Contoured support pillow"></div><h3>Nightline II Machine Starter Kit</h3><div class="price"><s>$940.00</s>$690.00</div><a class="btn-sm" href="#">Add to Cart</a></article>
  </div>
</section>

<section class="premium">
  <div class="premium-photo" role="img" aria-label="Person sleeping peacefully, soft faded backdrop"></div>
  <div class="premium-product" role="img" aria-label="Premium sleep therapy machine with display"></div>
  <div class="premium-copy">
    <h2>Premium Range</h2>
    <div class="amount">$345.00 <small>Per Month</small></div>
    <p>Our premium machines are quiet, compact and simple to use, with clear displays and smart comfort settings that adjust through the night.</p>
    <p>Flexible monthly payments let you choose the best equipment without a large upfront cost, and our team supports you every step of the way.</p>
  </div>
</section>

<section class="testimonials">
  <h2 class="section-title">Testimonials</h2>
  <div class="quotes">
    <div class="quote">
      <p>"The team explained every option clearly and found me a machine I could afford. I sleep through the night now and wake up with energy I had forgotten I had."</p>
      <div class="author"><span class="avatar" role="img" aria-label="Customer portrait"></span><div><b>MIRA DALTON</b><span class="stars"><svg width="80" height="14" viewBox="0 0 80 14"><g fill="#f5b800"><path id="st" d="M7 0l2 5h5l-4 3 2 5-5-3-5 3 2-5-4-3h5z"/><use href="#st" x="16"/><use href="#st" x="32"/><use href="#st" x="48"/><use href="#st" x="64"/></g></svg></span></div></div>
    </div>
    <div class="quote">
      <p>"Honest advice, fair prices and friendly follow up. After years of poor sleep I finally feel rested, and my wife says the snoring has stopped for good."</p>
      <div class="author"><span class="avatar" role="img" aria-label="Customer portrait"></span><div><b>GLEN HARTLEY</b><span class="stars"><svg width="80" height="14" viewBox="0 0 80 14"><g fill="#f5b800"><use href="#st"/><use href="#st" x="16"/><use href="#st" x="32"/><use href="#st" x="48"/><use href="#st" x="64"/></g></svg></span></div></div>
    </div>
  </div>
</section>

<section class="newsletter">
  <div>
    <h2>Stay up to date</h2>
    <p>Join our mailing list and receive <b>$50</b> discount</p>
  </div>
  <form class="subscribe"><input type="email" value="Enter email address"><button type="button">Subscribe</button></form>
</section>

<footer class="site-footer">
  <a class="brand" href="#"><span class="brand-mark"></span>RestWell Supply</a>
  <div class="footer-links">
    Home &nbsp;|&nbsp; About Us &nbsp;|&nbsp; Contact Us &nbsp;|&nbsp; Franchise &nbsp;|&nbsp; New Arrivals &nbsp;|&nbsp; Finance &nbsp;|&nbsp; SHOP<br>
    Copyright © RestWell Supply 2017. All Rights Reserved.
  </div>
  <div class="follow">Follow Us <i></i><i></i><i></i><i></i></div>
</footer>

</div>
</body>
</html>
```